Business Card

We would like a very clean corporate, two sided business card that conveys that we are a quality focused, reliable organisation that can make a business better. We focus on a cycle of continuous improvement for IT systems.

The brief is primarily clean and corporate, nothing overly complicated.

We sell IT services, IT support, server implementation, problem solving services to businesses in Australia.

Business

```html
<!DOCTYPE html>
<html lang="en">
<head>
<meta charset="utf-8">
<title>Keystone Loop — Business Card</title>
<link href="https://fonts.googleapis.com/css2?family=Open+Sans:wght@400;600;700&display=swap" rel="stylesheet">
<style>
  :root {
    --page: #ecebe8;
    --card-light: #ffffff;
    --card-mid: #e6e6e6;
    --navy: #272a3d;
    --crimson: #d01044;
    --logo-ink: #272a3d;
    --white: #ffffff;
    --muted: #3a3a3a;
  }
  * { margin: 0; padding: 0; box-sizing: border-box; }
  html, body {
    width: 1200px; height: 900px; overflow: hidden;
    background: var(--page);
    font-family: "Open Sans", Arial, sans-serif;
  }
  .stage { position: relative; width: 1200px; height: 900px; }

  .card {
    position: absolute; top: 300px;
    width: 504px; height: 288px;
    border-radius: 18px; overflow: hidden;
    background: linear-gradient(90deg, var(--card-light) 0%, var(--card-mid) 100%);
    box-shadow: 0 4px 12px rgba(0,0,0,0.18);
  }
  .card--front { left: 77px; }
  .card--back { left: 625px; }

  .wordmark {
    position: absolute; left: 0; right: 0;
    display: flex; align-items: center; justify-content: center; gap: 12px;
    color: var(--logo-ink); font-weight: 600; font-size: 36px; line-height: 44px;
    letter-spacing: -0.5px; white-space: nowrap;
  }
  .wordmark__mark { width: 18px; height: 18px; background: var(--crimson); }
  .card--front .wordmark { top: 66px; }
  .card--back .wordmark { top: 124px; }

  /* front */
  .front__band { position: absolute; left: 0; right: 0; top: 161px; height: 12px; background: var(--navy); }
  .front__panel {
    position: absolute; left: 0; right: 0; top: 173px; bottom: 0;
    background: var(--crimson); color: var(--white);
  }
  .holder { position: absolute; left: 0; right: 0; top: 2px; text-align: center; }
  .holder__name { font-size: 18px; font-weight: 700; line-height: 24px; }
  .holder__role { font-size: 13.5px; line-height: 18px; }
  .contact__col {
    position: absolute; top: 52px;
    font-size: 9.6px; line-height: 13.5px; white-space: nowrap;
  }
  .contact__col--address { left: 28px; }
  .contact__col--phone { left: 208px; }
  .contact__col--mail { left: 332px; }
  .contact__divider {
    position: absolute; top: 58px; width: 1px; height: 36px;
    background: rgba(255,255,255,0.85);
  }
  .contact__divider--one { left: 198px; }
  .contact__divider--two { left: 319px; }
  .contact__company { font-weight: 700; }

  /* back */
  .back__url {
    position: absolute; left: 0; right: 0; top: 232px; text-align: center;
    font-size: 13px; line-height: 16px; letter-spacing: 2.6px; color: var(--muted);
    white-space: nowrap;
  }
  .back__band { position: absolute; left: 0; right: 0; top: 259px; height: 13px; background: var(--navy); }
  .back__stripe { position: absolute; left: 0; right: 0; top: 272px; bottom: 0; background: var(--crimson); }
</style>
</head>
<body>
<main class="stage">
  <section class="card card--front" aria-label="Business card front">
    <div class="wordmark"><span>keystone loop</span><span class="wordmark__mark"></span></div>
    <div class="front__band"></div>
    <div class="front__panel">
      <div class="holder">
        <p class="holder__name">MT Collins</p>
        <p class="holder__role">President</p>
      </div>
      <div class="contact__col contact__col--address">
        <p class="contact__company">Keystone Loop Pty Ltd</p>
        <p>Suite 210, 14-18 Alder Street</p>
        <p>Chatswood, NSW, 2067 Australia</p>
      </div>
      <span class="contact__divider contact__divider--one"></span>
      <div class="contact__col contact__col--phone">
        <p>&nbsp;</p>
        <p>PH: +61 2 9100 4812</p>
        <p>FAX: +61 2 9100 4839</p>
      </div>
      <span class="contact__divider contact__divider--two"></span>
      <div class="contact__col contact__col--mail">
        <p>&nbsp;</p>
        <p>MAIL : collins@keystoneloop.net</p>
        <p>ABN: 48 117 305 629</p>
      </div>
    </div>
  </section>

  <section class="card card--back" aria-label="Business card back">
    <div class="wordmark"><span>keystone loop</span><span class="wordmark__mark"></span></div>
    <p class="back__url">www.keystoneloop.net</p>
    <div class="back__band"></div>
    <div class="back__stripe"></div>
  </section>
</main>
</body>
</html>
```